Book Cover "Venice"

Creation of a cover (14 x 20.5 cm + bleed area) for a book:
Image: “BrumeVerte” (Tiff joined)
AUTHOR: Corinne Valmer
TITLE: The murmurs of Lorient
PUBLISHER: Editions Pluvane (AT THE BOTTOM OF THE COVER)

Target Market(s)

Readers of romantic novels

Industry/Entity Type

Book

```html
<!DOCTYPE html>
<html lang="en">
<head>
<meta charset="utf-8">
<title>The Murmurs of Lorient — Corinne Valmer</title>
<link rel="stylesheet" href="https://fonts.googleapis.com/css2?family=Bebas+Neue&display=swap">
<style>
  :root {
    --sky-top: #4a1418;
    --sky-high: #b5161a;
    --sky-mid: #dc2418;
    --sky-glow: #ea5a1e;
    --sky-low: #b8201a;
    --dusk: #1c0a0b;
    --ink: #ffffff;
    --ghost: rgba(255, 255, 255, 0.11);
  }
  html, body {
    margin: 0;
    padding: 0;
    width: 820px;
    height: 1200px;
    overflow: hidden;
    background: #222;
  }
  .cover {
    position: relative;
    width: 820px;
    height: 1200px;
    overflow: hidden;
    font-family: "Bebas Neue", "Oswald", sans-serif;
    color: var(--ink);
  }
  .cover__photo {
    position: absolute;
    inset: 0;
    background:
      radial-gradient(ellipse 70% 30% at 55% 58%, rgba(240, 110, 40, 0.55), transparent 70%),
      linear-gradient(180deg,
        var(--sky-top) 0%,
        var(--sky-high) 14%,
        var(--sky-mid) 38%,
        var(--sky-glow) 56%,
        var(--sky-low) 70%,
        #5a1512 82%,
        var(--dusk) 92%,
        var(--dusk) 100%);
  }
  .cover__ghost {
    position: absolute;
    left: 18px;
    top: 40px;
    margin: 0;
    font-size: 262px;
    line-height: 0.86;
    color: var(--ghost);
    white-space: nowrap;
    pointer-events: none;
  }
  .cover__ghost span { display: block; }
  .title {
    position: absolute;
    left: 0;
    right: 0;
    top: 44px;
    margin: 0;
    text-align: center;
    font-weight: 400;
  }
  .title__the {
    display: block;
    font-size: 120px;
    line-height: 1;
    height: 104px;
  }
  .title__main {
    display: block;
    font-size: 220px;
    line-height: 1;
    height: 196px;
    margin-left: 8px;
  }
  .title__of {
    display: flex;
    align-items: center;
    justify-content: center;
    gap: 16px;
    width: 646px;
    margin: 0 auto;
    height: 52px;
    font-size: 64px;
    line-height: 1;
  }
  .title__of::before,
  .title__of::after {
    content: "";
    flex: 1;
    height: 5px;
    background: var(--ink);
  }
  .title__place {
    display: block;
    font-size: 272px;
    line-height: 1;
    height: 232px;
    margin-left: 10px;
  }
  .author {
    position: absolute;
    left: 108px;
    width: 640px;
    top: 626px;
    margin: 0;
    font-size: 52px;
    line-height: 1;
    display: flex;
    justify-content: space-between;
    font-weight: 400;
  }
  .publisher {
    position: absolute;
    left: 0;
    right: 0;
    bottom: 18px;
    margin: 0;
    text-align: center;
    font-size: 30px;
    letter-spacing: 0.5px;
  }
</style>
</head>
<body>
  <main class="cover">
    <div class="cover__photo" role="img" aria-label="BrumeVerte photograph: blazing red and orange sunset sky over a harbour skyline of domes and bell towers in dark silhouette, with glowing street lanterns in the foreground"></div>

    <p class="cover__ghost" aria-hidden="true">
      <span>LORIENT</span>
      <span>LORIENT</span>
      <span>LORIENT</span>
      <span>LORIENT</span>
      <span>LORIENT</span>
    </p>

    <h1 class="title">
      <span class="title__the">THE</span>
      <span class="title__main">MURMURS</span>
      <span class="title__of">OF</span>
      <span class="title__place">LORIENT</span>
    </h1>

    <p class="author" aria-label="Corinne Valmer">
      <span>C</span><span>O</span><span>R</span><span>I</span><span>N</span><span>N</span><span>E</span>
      <span>&nbsp;</span>
      <span>V</span><span>A</span><span>L</span><span>M</span><span>E</span><span>R</span>
    </p>

    <p class="publisher">PUBLISHER: EDITIONS PLUVANE</p>
  </main>
</body>
</html>
```